New Zealand health product business needs website designed

A website is required for a business that sells New Zealand made products, namely products like infant formula, health products such as NZ honey, supplements, skincare products etc. This is purely an informative website that will introduce the all the different types of products the business has to offer. The target audience will the the Chinese market. The logo is a calligraphy style font in colours 78b643 and 313542 (logo is still being finalised at the moment) so a colour theme to match would be great.

It is crucial that the design communicates the beautiful nature of New Zealand, non-polluted environments, with emphasis on pure, natural and cleaniness.
Updates

A website that I quite like is http://www.frostvalegelato.co.nz

Information is easy to find, layout is nice and clear.                          

Hi all, I have now uploaded a logo for the business "Tawny Crate", please note that this is yet to be finalized however I expect it to be minor changes so please ensure the website theme and colour use go well with the logo. 

There are three scenery images uploaded, designs with any one of them used is fine whichever works better with your design.  Only one image is required on the website, no sliding effects for this.

Also just to clarify my requirements further.  The developer can use HTML, PHP, Javascript, CSS for coding, preferably to have the images cut and a pdf guide provided for things like alignment and sizing etc.

The menu items are Home / Our story / Product outline / Brands / Contact us
Designs are required for all these.  Within the product outline page, the subcategories are -
Infant formulas
Baby supplements
Toddlers products
Honey
Beauty products
Mens supplements
Womens supplements
Health products
Others

   

Target Market(s)

China based customers looking for quality products from New Zealand.

Industry/Entity Type

Health

Requirements
Must have
• clear menu bar in home page, the four main menu items are -
Our story
Product outline
Brands
Contact us
Nice to have
• Space for a large scenery photo in the home page

```html
<!DOCTYPE html>
<html lang="en">
<head>
<meta charset="utf-8">
<title>Tawny Crate – Infant formulas</title>
<link rel="stylesheet" href="https://fonts.googleapis.com/css2?family=Arimo:wght@400&family=Questrial&display=swap">
<style>
  :root {
    --page-bg: #f4f4ef;
    --white: #ffffff;
    --line: #dcdcd6;
    --leaf: #78b643;
    --lime: #7ab51d;
    --deep-green: #4a962c;
    --ink: #313542;
    --text: #999999;
    --muted: #777777;
    --orange-a: #fcc41a;
    --orange-b: #f7901e;
    --tab-bg: #f7f7f3;
    --ui-font: "Questrial", "Century Gothic", sans-serif;
    --body-font: "Arimo", Arial, sans-serif;
  }
  * { box-sizing: border-box; margin: 0; padding: 0; }
  html, body { width: 1200px; height: 1000px; overflow: hidden; }
  body { background: var(--page-bg); font-family: var(--body-font); color: var(--text); position: relative; }
  .abs { position: absolute; }

  /* Header */
  .brand { left: 162px; top: 18px; display: flex; align-items: center; gap: 12px;
    font-family: var(--ui-font); font-size: 44px; color: var(--leaf); line-height: 1; }
  .brand-dot { width: 16px; height: 16px; border-radius: 50%; background: var(--leaf); }
  .contact { right: 229px; top: 13px; text-align: right; font-size: 10px; line-height: 11.7px; color: #666; }
  .contact h2 { font-weight: 400; font-size: 14px; color: #555; margin-bottom: 12px; }

  /* Navigation */
  .main-nav { left: 0; top: 98px; width: 1200px; height: 44px; background: var(--white);
    border-top: 1px solid var(--line); border-bottom: 1px solid var(--line); }
  .main-nav a { position: absolute; top: 13px; font-family: var(--ui-font); font-size: 14px;
    color: var(--deep-green); text-decoration: none; }
  .main-nav a.current { color: var(--ink); }
  .nav-sep { position: absolute; top: 12px; width: 1px; height: 22px; background: #e6e6e2; }

  /* Breadcrumbs */
  .breadcrumb { left: 162px; top: 157px; font-size: 10px; color: var(--deep-green); }
  .breadcrumb a { color: var(--deep-green); }
  .trail { left: 162px; top: 180px; width: 593px; height: 27px; border-top: 1px solid var(--line);
    border-bottom: 1px solid var(--line); font-size: 12px; color: var(--lime); padding: 6px 1px; }

  /* Product */
  .product { left: 162px; top: 219px; width: 593px; height: 224px; background: var(--white); border: 1px solid var(--line); }
  .product-photo { position: absolute; left: 13px; top: 14px; width: 206px; height: 193px; background: var(--white); border: 1px solid var(--line); }
  .product-info { position: absolute; left: 230px; top: 14px; width: 350px; }
  .product-info h1 { font-weight: 400; font-size: 15px; color: var(--lime); margin-bottom: 14px; }
  .product-info p { font-size: 10px; line-height: 14.5px; margin-bottom: 14px; }
  .price-label { font-size: 10px; color: var(--deep-green); margin-top: 3px; }
  .price { font-size: 10px; color: #333; margin-top: 9px; }

  /* Tabs */
  .tabs { left: 162px; top: 469px; display: flex; }
  .tab { height: 38px; border: 1px solid var(--line); border-left: none; background: var(--tab-bg);
    font-size: 10px; color: var(--text); display: flex; align-items: center; justify-content: center; }
  .tab:first-child { border-left: 1px solid var(--line); background: var(--white); color: var(--orange-b); border-bottom-color: var(--white); border-radius: 6px 0 0 0; }
  .tab-panel { left: 162px; top: 506px; width: 593px; height: 161px; background: var(--white);
    border: 1px solid var(--line); border-radius: 0 0 9px 9px; padding: 24px 21px; }
  .tab-panel p { font-size: 10px; line-height: 14.5px; margin-bottom: 14px; }
  .tab-cover { left: 163px; top: 505px; width: 83px; height: 2px; background: var(--white); }

  /* Sidebar */
  .search { left: 761px; top: 178px; width: 212px; height: 96px; }
  .search-label { position: absolute; left: 18px; top: 18px; font-size: 12px; color: var(--white); }
  .search-field { position: absolute; left: 17px; top: 39px; width: 179px; height: 30px; background: var(--white); }
  .search-btn { position: absolute; right: 0; top: 0; width: 36px; height: 30px; background: #efefec;
    display: flex; align-items: center; justify-content: center; }
  .promo { left: 772px; top: 290px; width: 201px; height: 208px; border-radius: 8px;
    background: linear-gradient(160deg, #a8c92a 0%, #94c01f 55%, #86b81c 100%); }

  /* Product strip */
  .products { left: 161px; top: 717px; width: 811px; height: 233px; background: var(--white); border: 1px solid #e4e4de; }
  .products h2 { position: absolute; left: 15px; top: 19px; font-weight: 400; font-size: 15px; color: #333; }
  .products-rule { position: absolute; left: 15px; top: 41px; width: 780px; height: 1px; background: var(--line); }
  .pager { position: absolute; top: 20px; width: 16px; height: 17px; color: var(--white); font-size: 9px;
    display: flex; align-items: center; justify-content: center; }
  .pager.prev { left: 757px; background: #dcdcd8; }
  .pager.next { left: 778px; background: var(--deep-green); }
  .card { position: absolute; top: 65px; width: 170px; }
  .card h3 { font-weight: 400; font-size: 11px; color: var(--muted); margin-bottom: 12px; }
  .card p { font-size: 10px; line-height: 14.5px; }
  .card a { display: block; margin-top: 17px; margin-left: 2px; font-size: 10px; color: var(--deep-green); text-decoration: none; }
  .card-sep { position: absolute; top: 77px; width: 1px; height: 122px; background: #e8e8e4; }

  /* Footer */
  .footer-rule { left: 162px; top: 970px; width: 810px; height: 1px; background: var(--line); }
  .social { top: 977px; width: 20px; height: 20px; border: 1px solid #cfcfca; border-radius: 3px; background: var(--white); }
  .social span { position: absolute; left: 6px; top: 6px; width: 6px; height: 6px; background: #555; }
  .copyright { right: 229px; top: 980px; font-size: 8px; color: var(--muted); }
</style>
</head>
<body>

<header>
  <div class="brand abs"><span class="brand-dot"></span>Tawny Crate</div>
  <address class="contact abs" style="font-style:normal">
    <h2>Contact Us:</h2>
    #234, Tawny Crate, UK<br>
    Example of address goes here<br>
    Call: 1234 567<br>
    info@example.com
  </address>
</header>

<nav class="main-nav abs">
  <a href="#" style="left:162px">Home</a>
  <span class="nav-sep" style="left:223px"></span>
  <a href="#" style="left:245px">Our Story</a>
  <span class="nav-sep" style="left:318px"></span>
  <a href="#" class="current" style="left:338px">Product Outline</a>
  <span class="nav-sep" style="left:443px"></span>
  <a href="#" style="left:460px">Brands</a>
  <span class="nav-sep" style="left:520px"></span>
  <a href="#" style="left:539px">Contact Us</a>
</nav>

<div class="breadcrumb abs"><a href="#">Home</a> &gt; Bredscrum Goes Here</div>
<div class="trail abs">Name of the product, display here &gt; Infant formulas</div>

<section class="product abs">
  <div class="product-photo" role="img" aria-label="Product photo of infant formula"></div>
  <div class="product-info">
    <h1>Infant formulas</h1>
    <p>Lorem Ipsum is simply dummy text of the printing and typesetting industry. Lorem Ipsum has been the industry's standardLorem Ipsum is simply dummy text of the printing and typesetting industry. Lorem Ipsum has been the industry's standard Lorem Ipsum is simply dummy text of the printing and typesetting industry. Lorem Ipsum has been the industry's standard</p>
    <p>Lorem Ipsum is simply dummy text of the printing and typesetting industry. Lorem Ipsum has been the industry's standard</p>
    <div class="price-label">PRODUCT PRICE</div>
    <div class="price">$34.45</div>
  </div>
</section>

<div class="tabs abs">
  <div class="tab" style="width:86px">More Info</div>
  <div class="tab" style="width:92px">Lorem Ipsum</div>
  <div class="tab" style="width:92px">Lorem Ipsum</div>
</div>
<section class="tab-panel abs">
  <p>Lorem Ipsum is simply dummy text of the printing and typesetting industry. Lorem Ipsum has been the industry's standard Lorem Ipsum is simply dummy text of the printing and typesetting industry. Lorem Ipsum has been the industry's standard</p>
  <p>Lorem Ipsum is simply dummy text of the printing and typesetting industry. Lorem Ipsum has been the industry's standardLorem Ipsum is simply dummy text of the printing and typesetting industry. Lorem Ipsum has been the industry's standard</p>
</section>
<div class="tab-cover abs"></div>

<aside>
  <div class="search abs">
    <svg width="212" height="96" viewBox="0 0 212 96" style="position:absolute;left:0;top:0">
      <defs>
        <linearGradient id="searchFill" x1="0" y1="0" x2="1" y2="0.4">
          <stop offset="0" stop-color="#fcc41a"/>
          <stop offset="1" stop-color="#f7901e"/>
        </linearGradient>
      </defs>
      <path d="M8 0 H204 Q212 0 212 8 V78 Q212 86 204 86 H14 V96 Q3 90 0 80 V8 Q0 0 8 0 Z" fill="url(#searchFill)"/>
    </svg>
    <div class="search-label">Search</div>
    <div class="search-field">
      <div class="search-btn">
        <svg width="18" height="18" viewBox="0 0 18 18"><circle cx="7" cy="7" r="5.2" fill="none" stroke="#8a8a8a" stroke-width="1.4"/><line x1="11" y1="11" x2="16" y2="16" stroke="#8a8a8a" stroke-width="2" stroke-linecap="round"/></svg>
      </div>
    </div>
  </div>
  <div class="promo abs"></div>
</aside>

<section class="products abs">
  <h2>Products</h2>
  <div class="products-rule"></div>
  <div class="pager prev">&lt;</div>
  <div class="pager next">&gt;</div>

  <div class="card" style="left:17px">
    <h3>Infant formulas</h3>
    <p>Lorem Ipsum is simply dummy text of the printing and typesetting industry. Lorem Ipsum has been the industry's standard</p>
    <a href="#">read more..</a>
  </div>
  <span class="card-sep" style="left:193px"></span>
  <div class="card" style="left:214px">
    <h3>Baby supplements</h3>
    <p>Lorem Ipsum is simply dummy text of the printing and typesetting industry. Lorem Ipsum has been the industry's standard</p>
    <a href="#">read more..</a>
  </div>
  <span class="card-sep" style="left:397px"></span>
  <div class="card" style="left:420px">
    <h3>Toddlers products</h3>
    <p>Lorem Ipsum is simply dummy text of the printing and typesetting industry. Lorem Ipsum has been the industry's standard</p>
    <a href="#">read more..</a>
  </div>
  <span class="card-sep" style="left:605px"></span>
  <div class="card" style="left:632px">
    <h3>Honey</h3>
    <p>Lorem Ipsum is simply dummy text of the printing and typesetting industry. Lorem Ipsum has been the industry's standard</p>
    <a href="#">read more..</a>
  </div>
</section>

<footer>
  <div class="footer-rule abs"></div>
  <a class="social abs" href="#" aria-label="Social link" style="left:163px"><span></span></a>
  <a class="social abs" href="#" aria-label="Social link" style="left:191px"><span></span></a>
  <a class="social abs" href="#" aria-label="Social link" style="left:220px"><span></span></a>
  <a class="social abs" href="#" aria-label="Feed" style="left:248px"><span></span></a>
  <div class="copyright abs">Copyright 2013 All Right Reserved</div>
</footer>

</body>
</html>
```